BRQL project
Cloudward Trainer Bench Systems
i dont see, button or anything ,,,...
about handover...anyone help me..??
i am first in here..how way the rule and upload my file to ch....
The project has been extended for 3 more days.
Ruth.
Hi,
I want only static
hello ! my name is Ida :) I want to participate this nice contest ~! Haven't one .ai format logo ? I not understand static or animated banner !? please more details - thanks
or not of*
flash of animated gif?
I would like to see it animated also
Do you need it animated?
I would like to see also a new with the wgt lifter text to be replaced by Vortek WGT PC.
Also add the bellow text
Increase WGT performance by 30% and more
It would be great if you could give specific text content / copy. Please mention your preferred colors and other specifications(if any). A more detailed design brief would help.

```html
<!DOCTYPE html>
<html lang="en">
<head>
<meta charset="utf-8">
<title>Vortek WGT PC – Banner Set</title>
<link rel="stylesheet" href="https://fonts.googleapis.com/css2?family=Open+Sans:wght@600;700;800&display=swap">
<style>
  :root {
    --stage: #000000;
    --sky-top: #3d8fd6;
    --sky-mid: #8cc0ea;
    --sky-low: #d9ecf8;
    --navy: #0b2a78;
    --royal: #1a48b4;
    --orange: #f39a16;
    --white: #ffffff;
    --silver-hi: #ffffff;
    --silver-lo: #8a9bb0;
    --badge-ink: #1a3d8f;
  }
  * { box-sizing: border-box; margin: 0; padding: 0; }
  html, body { width: 1200px; height: 845px; overflow: hidden; background: var(--stage); }
  body { position: relative; font-family: "Open Sans", Arial, sans-serif; }

  .banner { position: absolute; overflow: hidden; background: var(--navy); }
  .banner--skyscraper { left: 60px; top: 53px; width: 192px; height: 727px; }
  .banner--leaderboard { left: 264px; top: 197px; width: 883px; height: 110px; }
  .banner--rectangle { left: 264px; top: 324px; width: 367px; height: 305px; }

  .sky-photo { position: absolute; inset: 0;
    background: radial-gradient(ellipse at 35% 55%, var(--sky-low) 0%, var(--sky-mid) 40%, var(--sky-top) 100%); }

  .wave { position: absolute; inset: 0; width: 100%; height: 100%; }

  .title {
    position: absolute; font-weight: 800; text-transform: uppercase;
    line-height: 0.98; text-align: center; letter-spacing: 1px;
    background: linear-gradient(180deg, var(--silver-hi) 10%, #dfe6ef 45%, var(--silver-lo) 100%);
    -webkit-background-clip: text; background-clip: text; color: transparent;
    filter: drop-shadow(1px 2px 1px rgba(10,30,80,0.55));
  }

  .badge {
    position: absolute; border-radius: 50%; background: var(--white);
    display: flex; align-items: center; justify-content: center;
    box-shadow: 0 1px 3px rgba(0,0,0,0.35);
  }
  .badge__name { font-weight: 800; color: var(--badge-ink); letter-spacing: 1px; }

  .offer { position: absolute; font-weight: 800; text-transform: uppercase; line-height: 1.05; }
  .offer__lead { color: var(--orange); display: block; }
  .offer__main { color: var(--white); display: block; }
  .offer__by { color: var(--white); font-weight: 700; text-transform: none; }
  .offer__pct { color: var(--orange); }
  .offer__more { color: var(--white); font-weight: 700; text-transform: none; }

  /* skyscraper */
  .banner--skyscraper .title { left: 0; right: 0; top: 28px; font-size: 36px; }
  .banner--skyscraper .badge { left: 52px; top: 486px; width: 88px; height: 88px; }
  .banner--skyscraper .badge__name { font-size: 20px; }
  .banner--skyscraper .offer { left: 0; right: 0; top: 600px; text-align: center; }
  .banner--skyscraper .offer__lead { font-size: 21px; }
  .banner--skyscraper .offer__main { font-size: 18px; }
  .banner--skyscraper .offer__by { font-size: 18px; }
  .banner--skyscraper .offer__pct { font-size: 38px; }
  .banner--skyscraper .offer__more { display: block; font-size: 18px; }

  /* leaderboard */
  .banner--leaderboard .title { left: 150px; width: 250px; top: 12px; font-size: 38px; }
  .banner--leaderboard .badge { left: 530px; top: 25px; width: 60px; height: 60px; }
  .banner--leaderboard .badge__name { font-size: 14px; }
  .banner--leaderboard .offer { left: 615px; top: 16px; }
  .banner--leaderboard .offer__lead { font-size: 26px; }
  .banner--leaderboard .offer__main { font-size: 21px; }
  .banner--leaderboard .offer__by { font-size: 17px; }
  .banner--leaderboard .offer__pct { font-size: 22px; }
  .banner--leaderboard .offer__more { font-size: 14px; }

  /* rectangle */
  .banner--rectangle .title { left: 150px; width: 215px; top: 14px; font-size: 41px; }
  .banner--rectangle .badge { left: 276px; top: 108px; width: 74px; height: 74px; }
  .banner--rectangle .badge__name { font-size: 17px; }
  .banner--rectangle .offer { left: 12px; top: 236px; }
  .banner--rectangle .offer__lead { font-size: 25px; }
  .banner--rectangle .offer__main { font-size: 19px; }
  .banner--rectangle .offer__by { font-size: 19px; }
  .banner--rectangle .offer__pct { font-size: 23px; }
  .banner--rectangle .offer__more { font-size: 15px; }
</style>
</head>
<body>

<section class="banner banner--skyscraper" aria-label="Vortek WGT PC skyscraper banner">
  <div class="sky-photo" role="img" aria-label="Photo of a white business jet banking through a blue sky with clouds"></div>
  <svg class="wave" viewBox="0 0 192 727" preserveAspectRatio="none" aria-hidden="true">
    <defs>
      <linearGradient id="skyBand" x1="0" y1="0" x2="0" y2="1">
        <stop offset="0" stop-color="#1a48b4"/><stop offset="1" stop-color="#0b2a78"/>
      </linearGradient>
    </defs>
    <path d="M0 470 Q96 445 192 505 L192 727 L0 727 Z" fill="url(#skyBand)"/>
    <path d="M0 462 Q96 436 192 497 L192 508 Q96 452 0 474 Z" fill="#f39a16"/>
  </svg>
  <h2 class="title">Vortek<br>WGT PC</h2>
  <div class="badge"><span class="badge__name">BRQL</span></div>
  <p class="offer">
    <span class="offer__lead">Increase WGT</span>
    <span class="offer__main">Performance</span>
    <span class="offer__by">by </span><span class="offer__pct">30%</span>
    <span class="offer__more">and more!</span>
  </p>
</section>

<section class="banner banner--leaderboard" aria-label="Vortek WGT PC leaderboard banner">
  <div class="sky-photo" role="img" aria-label="Photo of a white business jet banking through a blue sky with clouds"></div>
  <svg class="wave" viewBox="0 0 883 110" preserveAspectRatio="none" aria-hidden="true">
    <path d="M600 0 Q585 70 555 110 L883 110 L883 0 Z" fill="url(#skyBand)"/>
    <path d="M300 110 Q500 104 590 0 L604 0 Q580 80 550 110 Z" fill="#f39a16"/>
  </svg>
  <h2 class="title">Vortek<br>WGT PC</h2>
  <div class="badge"><span class="badge__name">BRQL</span></div>
  <p class="offer">
    <span class="offer__lead">Increase WGT</span>
    <span class="offer__main">Performance</span>
    <span class="offer__by">by </span><span class="offer__pct">30%</span><span class="offer__more"> and more!</span>
  </p>
</section>

<section class="banner banner--rectangle" aria-label="Vortek WGT PC rectangle banner">
  <div class="sky-photo" role="img" aria-label="Photo of a white business jet banking through a blue sky with clouds"></div>
  <svg class="wave" viewBox="0 0 367 305" preserveAspectRatio="none" aria-hidden="true">
    <path d="M0 232 Q180 180 367 196 L367 305 L0 305 Z" fill="url(#skyBand)"/>
    <path d="M0 224 Q180 170 367 186 L367 197 Q180 184 0 236 Z" fill="#f39a16"/>
  </svg>
  <h2 class="title">Vortek<br>WGT PC</h2>
  <div class="badge"><span class="badge__name">BRQL</span></div>
  <p class="offer">
    <span class="offer__lead">Increase WGT</span>
    <span class="offer__main">Performance <span class="offer__by">by </span><span class="offer__pct">30%</span><span class="offer__more"> and more!</span></span>
  </p>
</section>

</body>
</html>
```